Business Card Design

We need a business card designed for a new company based in Melbourne called KPo solutions. KPo solutions provides management consulting specialising in the health and social services sector.

KPo solutions offer a unique set of specialist skills │dealing with all levels of government │ unique communication skills│intimate knowledge of the health sector │solutions tailored to unique circumstances.

KPo solutions takes on a select number of clients at any one time, this ensures that your organisation receives the attention required. On larger projects, KPo solutions join up with other consultants to bring specialist skills to a project.
Updates

This is the first time I have used Pattern Hive and thank you all for responding. The variation is amazing and makes it hard to decide. I have to ask some of my friends to give me their views. The response is fantastic. The one I pick will basically be the most visually appealing

Industry/Entity Type

Management Consulting

Contact Information for Business Card

Martin Hollis, Principal, KPo solutions, 14 Calloway Ave, Westbridge VIC 3094, 0438 712 304, martinh@kposolutions.com.au, www.kposolutions.com.au

```html
<!DOCTYPE html>
<html lang="en">
<head>
<meta charset="utf-8">
<title>KPo solutions – Business Card</title>
<link rel="stylesheet" href="https://fonts.googleapis.com/css2?family=Crimson+Pro:ital,wght@0,600;1,700&display=swap">
<style>
  :root {
    --backdrop: #e9e6e2;
    --card-white: #fbfaf9;
    --brand-red: #a5171d;
    --brand-red-dark: #8e1217;
    --ink-red: #7a1418;
    --underline-pink: #e8cfcb;
    --text-white: #ffffff;
  }
  * { margin: 0; padding: 0; box-sizing: border-box; }
  html, body {
    width: 1200px;
    height: 1000px;
    overflow: hidden;
    background: var(--backdrop);
  }
  .canvas {
    position: relative;
    width: 1200px;
    height: 1000px;
  }
  .business-card {
    position: absolute;
    left: 150px;
    top: 228px;
    width: 900px;
    height: 545px;
    background: linear-gradient(180deg, #ffffff 0%, var(--card-white) 100%);
    box-shadow: 0 6px 22px rgba(0, 0, 0, 0.18);
    overflow: hidden;
  }
  .brand-band {
    position: absolute;
    left: 0;
    top: 0;
    width: 100%;
    height: 232px;
    background: linear-gradient(180deg, var(--brand-red-dark) 0%, var(--brand-red) 100%);
  }
  .brand-mark {
    position: absolute;
    left: 88px;
    top: 66px;
    width: 100px;
    height: 100px;
    background: var(--card-white);
  }
  .brand-name {
    position: absolute;
    right: 56px;
    top: 84px;
    font-family: "Crimson Pro", serif;
    font-weight: 600;
    font-size: 56px;
    line-height: 1;
    letter-spacing: 2px;
    text-transform: uppercase;
    color: var(--text-white);
    white-space: nowrap;
  }
  .contact-block {
    position: absolute;
    right: 56px;
    top: 262px;
    text-align: right;
    font-family: "Crimson Pro", serif;
    color: var(--ink-red);
  }
  .person-line {
    display: inline-block;
    font-style: italic;
    font-weight: 700;
    font-size: 36px;
    line-height: 1.05;
    padding: 0 4px 2px 40px;
    background: linear-gradient(180deg, transparent 62%, var(--underline-pink) 62%);
  }
  .contact-details {
    margin-top: 10px;
    list-style: none;
    font-weight: 600;
    font-size: 21px;
    line-height: 1.4;
  }
</style>
</head>
<body>
  <main class="canvas">
    <article class="business-card">
      <header class="brand-band">
        <div class="brand-mark" aria-hidden="true"></div>
        <p class="brand-name">KPo solutions</p>
      </header>
      <section class="contact-block">
        <p class="person-line">Martin Hollis /Principal</p>
        <ul class="contact-details">
          <li>KPo solutions, 14 Calloway Ave</li>
          <li>Westbridge VIC 3094</li>
          <li>0438 712 304</li>
          <li>martinh@kposolutions.com.au</li>
          <li>www.kposolutions.com.au</li>
        </ul>
      </section>
    </article>
  </main>
</body>
</html>
```